Redesign of an insurance website

Attached is an insurance website that I need to redesign. Currently the website is too dark. I like for example www.brenvalo.com . Could you make the website lighter and change the structure a little so that it is more user friendly?

Industry/Entity Type

Insurance

Number of Pages Required

4 page

```html
<!DOCTYPE html>
<html lang="en">
<head>
<meta charset="utf-8">
<title>Krytoplan.cz – Financial Solutions</title>
<link href="https://fonts.googleapis.com/css2?family=Montserrat:wght@400;500;600;700;800&family=Open+Sans:wght@400;600&display=swap" rel="stylesheet">
<style>
:root{
  --navy:#0d2b5a;
  --navy-deep:#0a2149;
  --green:#0f6f60;
  --green-dark:#0b5a4e;
  --yellow:#f5d327;
  --blue-accent:#2f80d8;
  --ink:#1d2433;
  --text:#5d6470;
  --muted:#8a909a;
  --line:#dde1e6;
  --soft:#f3f4f7;
  --white:#fff;
}
*{box-sizing:border-box;margin:0;padding:0}
html,body{width:1200px;height:3871px;overflow:hidden}
body{font-family:"Open Sans",Arial,sans-serif;color:var(--text);background:var(--white);position:relative;font-size:13px;line-height:1.6}
h1,h2,h3,h4{font-family:"Montserrat",Arial,sans-serif;color:var(--ink)}
.section{position:absolute;left:0;width:1200px}
.ph{background:linear-gradient(135deg,#c9cfd6,#8e99a6)}

/* top bar */
.topbar{top:0;height:46px;background:var(--navy-deep);color:#c8d0de;font-size:12px}
.topbar .welcome{position:absolute;left:52px;top:13px}
.topbar .social{position:absolute;left:505px;top:15px;display:flex;gap:48px}
.topbar .social span{width:12px;height:12px;border-radius:50%;background:#c8d0de;display:block}
.topbar .search{position:absolute;right:64px;top:14px}

/* header */
.header{top:46px;height:101px;background:var(--green)}
.header .brand-area{position:absolute;left:0;top:0;width:440px;height:101px;background:var(--white);clip-path:polygon(0 0,100% 0,86% 100%,0 100%)}
.header .stripe{position:absolute;left:380px;top:0;width:70px;height:101px;background:var(--yellow);clip-path:polygon(30% 0,100% 0,70% 100%,0 100%)}
.brand{position:absolute;left:52px;top:34px;font-family:"Montserrat",sans-serif;font-weight:800;font-size:27px;color:var(--navy);letter-spacing:.5px}
.contact-item{position:absolute;top:32px;color:#fff;font-size:12px;line-height:1.3;display:flex;gap:14px;align-items:center}
.contact-item b{font-family:"Montserrat",sans-serif;font-weight:600;font-size:13px;display:block}
.btn-quote{position:absolute;right:52px;top:34px;width:148px;height:38px;background:var(--yellow);color:var(--ink);font-family:"Montserrat",sans-serif;font-weight:700;font-size:13px;display:flex;align-items:center;justify-content:center}

/* hero */
.hero{top:147px;height:426px;background:linear-gradient(90deg,#f1f4f6 0%,#e7ebee 38%,#b7c0c9 70%,#8d97a3 100%)}
.hero .photo{position:absolute;left:560px;top:0;width:640px;height:426px;background:linear-gradient(100deg,rgba(241,244,246,0) 0%,#a9b3bd 30%,#7b8694 100%)}
.nav{position:absolute;left:0;top:0;width:1200px;height:47px;display:flex;justify-content:center;gap:56px;align-items:center;font-family:"Montserrat",sans-serif;font-size:12px;font-weight:600;color:var(--navy)}
.hero .eyebrow{position:absolute;left:160px;top:140px;font-family:"Montserrat",sans-serif;font-weight:700;color:var(--green);font-size:18px;letter-spacing:.3px}
.hero h1{position:absolute;left:58px;top:166px;font-size:55px;font-weight:800;color:var(--green);letter-spacing:.5px;white-space:nowrap}
.hero p{position:absolute;left:108px;top:240px;width:520px;text-align:center;font-size:13px;color:#4d5563}
.btn-outline{position:absolute;border:1.5px solid var(--navy);color:var(--navy);font-family:"Montserrat",sans-serif;font-weight:600;font-size:12px;display:flex;align-items:center;justify-content:center}
.hero .btn-outline{left:284px;top:311px;width:148px;height:34px}
.hero .chat{position:absolute;right:30px;bottom:60px;width:40px;height:40px;border-radius:50%;background:var(--green)}

/* about */
.about{top:573px;height:627px}
.about .kicker{position:absolute;left:52px;top:100px;font-family:"Montserrat",sans-serif;font-weight:600;font-size:18px;color:var(--ink)}
.about .kicker span{color:var(--blue-accent)}
.about h2{position:absolute;left:52px;top:122px;font-size:25px;font-weight:600}
.about .copy{position:absolute;left:52px;top:170px;width:480px;font-size:12.5px}
.about .copy p{margin-bottom:18px}
.features{position:absolute;left:614px;top:168px;width:540px;display:grid;grid-template-columns:1fr 1fr;row-gap:28px;column-gap:24px}
.features h4,.service h4,.why-item h4{color:var(--green);font-size:16px;font-weight:600;margin-bottom:4px}
.features p{font-size:12.5px;line-height:1.55}
.about .team{position:absolute;top:370px;height:257px;width:300px;background:linear-gradient(180deg,#fff 0%,#d7dbe0 40%,#b3bac3 100%)}

/* chart */
.plan{top:1200px;height:524px;background:var(--soft)}
.plan svg{position:absolute;left:18px;top:140px}
.plan .kicker{position:absolute;left:614px;top:106px;font-family:"Montserrat",sans-serif;font-size:16px;font-weight:600;color:var(--green)}
.plan h2{position:absolute;left:614px;top:130px;font-size:25px;font-weight:600}
.plan .copy{position:absolute;left:614px;top:180px;width:570px;font-size:12.5px}
.plan .copy p{margin-bottom:14px}
.plan .btn-outline{left:614px;top:365px;width:128px;height:30px}

/* services */
.services{top:1724px;height:508px}
.services h2{position:absolute;left:0;width:1200px;top:100px;text-align:center;font-size:25px;font-weight:600}
.services .lead{position:absolute;left:300px;width:600px;top:142px;text-align:center;font-size:12.5px}
.service-grid{position:absolute;left:52px;top:222px;width:1096px;display:grid;grid-template-columns:repeat(3,1fr);row-gap:42px}
.service{position:relative;padding-left:60px}
.service svg{position:absolute;left:6px;top:4px}
.service p{font-size:12.5px;line-height:1.55;width:270px}

/* banner */
.banner{top:2232px;height:224px;background:linear-gradient(100deg,var(--green-dark),var(--green) 50%,#138774);text-align:center;color:#eaf4f1}
.banner h2{color:#fff;font-size:28px;font-weight:600;margin-top:42px}
.banner p{width:560px;margin:14px auto 0;font-size:13px}
.banner .btn-buy{position:absolute;left:550px;top:148px;width:100px;height:30px;background:#fff;color:var(--navy);font-family:"Montserrat",sans-serif;font-weight:600;font-size:12px;display:flex;align-items:center;justify-content:center}

/* why */
.why{top:2456px;height:318px}
.why .photo{position:absolute;left:0;top:0;width:556px;height:318px}
.why .kicker{position:absolute;left:580px;top:24px;font-family:"Montserrat",sans-serif;font-weight:600;font-size:16px;color:var(--green)}
.why h2{position:absolute;left:580px;top:44px;font-size:25px;font-weight:600}
.why .copy{position:absolute;left:580px;top:92px;width:590px;font-size:12.5px}
.why-grid{position:absolute;left:590px;top:178px;width:580px;display:grid;grid-template-columns:1fr 1fr;row-gap:16px;column-gap:20px}
.why-item{position:relative;padding-left:52px}
.why-item svg{position:absolute;left:0;top:2px}
.why-item p{font-size:12.5px;line-height:1.5;width:210px}

/* contact + faq */
.engage{top:2774px;height:658px}
.engage h3{position:absolute;top:156px;font-size:25px;font-weight:600}
.engage .intro{position:absolute;top:196px;width:530px;font-size:12.5px}
.field{position:absolute;height:34px;border:1px solid var(--line);font-size:12px;color:var(--muted);padding:8px 12px}
.btn-submit{position:absolute;left:52px;top:533px;width:124px;height:30px;background:var(--navy);color:#fff;font-family:"Montserrat",sans-serif;font-weight:700;font-size:12px;display:flex;align-items:center;justify-content:center}
.faq{position:absolute;left:670px;top:262px;width:480px}
.faq-item{display:flex;gap:16px;align-items:flex-start;font-size:12.5px;color:var(--ink);margin-bottom:20px}
.faq-item .mark{width:14px;height:14px;flex:none;margin-top:3px;border:1px solid var(--line);font-size:11px;line-height:12px;text-align:center;color:var(--muted)}
.faq-item.open .mark{background:var(--navy);color:#fff;border-color:var(--navy)}
.faq .answer{padding-left:46px;margin:-14px 0 24px;font-size:12.5px;width:360px}

/* footer */
.footer{top:3432px;height:388px;background:var(--navy);color:#c3cbdb;font-size:12.5px}
.footer .brand{position:absolute;left:52px;top:90px;color:#fff;font-size:25px}
.footer .about-text{position:absolute;left:52px;top:130px;width:250px;line-height:1.55}
.newsletter{position:absolute;left:52px;top:242px;width:250px;height:34px;border:1px solid #5b6f94;padding:7px 12px;font-size:11.5px}
.footer .col{position:absolute;top:86px}
.footer h4{color:#fff;font-size:14px;font-weight:600;margin-bottom:20px}
.footer .post b{display:block;color:#fff;font-weight:600;font-size:13px}
.footer .post{margin-bottom:20px;width:190px}
.footer ul{list-style:none;line-height:2.15}
.footer .contact-row{display:flex;gap:16px;margin-bottom:22px;align-items:flex-start}
.copyright{top:3820px;height:51px;background:var(--navy-deep);color:#c3cbdb;font-size:12px;text-align:center;line-height:51px}
</style>
</head>
<body>

<div class="section topbar">
  <div class="welcome">Welcome to Krytoplan.cz</div>
  <div class="social"><span></span><span></span><span></span><span></span></div>
  <svg class="search" width="16" height="16" viewBox="0 0 16 16"><circle cx="6.5" cy="6.5" r="4.5" fill="none" stroke="#c8d0de" stroke-width="2"/><line x1="10" y1="10" x2="14" y2="14" stroke="#c8d0de" stroke-width="2"/></svg>
</div>

<header class="section header">
  <div class="brand-area"></div>
  <div class="stripe"></div>
  <div class="brand">KRYTOPLAN.CZ</div>
  <div class="contact-item" style="left:465px">
    <svg width="24" height="24" viewBox="0 0 24 24"><path d="M6 3l4 4-2 3c1 3 3 5 6 6l3-2 4 4-3 3C10 21 3 14 3 6z" fill="none" stroke="#fff" stroke-width="1.6"/></svg>
    <div><b>(+91) 555-014-2309</b>We are open 9 am - 10pm</div>
  </div>
  <div class="contact-item" style="left:736px">
    <svg width="28" height="22" viewBox="0 0 28 22"><rect x="2" y="3" width="24" height="16" fill="none" stroke="#fff" stroke-width="1.6"/><path d="M2 3l12 9 12-9" fill="none" stroke="#fff" stroke-width="1.6"/></svg>
    <div><b>hello@krytoplan.cz</b>You can mail us</div>
  </div>
  <div class="btn-quote">GET A QUOTE</div>
</header>

<section class="section hero">
  <div class="photo" role="img" aria-label="Photo of two smiling business colleagues looking at a laptop"></div>
  <nav class="nav"><span>HOME</span><span>ABOUT US</span><span>CASES</span><span>SERVICES</span><span>PROJECTS</span><span>BLOG</span><span>SHOP</span><span>CONTACT</span></nav>
  <div class="eyebrow">WE PROVIDE BEST FINANCIAL SOLUTIONS</div>
  <h1>FOR YOUR BUSINESS</h1>
  <p>We have over 25 year's of experience in Finance and Business management so we can make your business more successful you can trust us</p>
  <div class="btn-outline">VIEW SERVICES</div>
  <div class="chat"></div>
</section>

<section class="section about">
  <div class="kicker">We are <span>KRYTOPLAN.CZ</span></div>
  <h2>Your Complete Financial Solutions</h2>
  <div class="copy">
    <p>Krytoplan amet, consectetur adipiscing elit, sed do eiusmod tempor ut labore et dolore magna aliqua. Ut enim ad minim iam, quis nostrud exercitation ullamco laboris nisi ut aliquip exea commo consequat. Duis aute irure dolor in reprehenderit</p>
    <p>Krytoplan amet, consectetur adipiscing elit, sed do eiusmod tempor incidi uitdfs on the labore et dolore magna aliqua enim ad minimiam.</p>
  </div>
  <div class="features">
    <div><h4>Financial Service</h4><p>Krytoplan consectetur adipiscing elit,<br>sed do eiusmod tempor incidunt</p></div>
    <div><h4>Best Consutancy</h4><p>Krytoplan consectetur adipiscing elit,<br>sed do eiusmod tempor incidunt</p></div>
    <div><h4>Business Analysis</h4><p>Krytoplan consectetur adipiscing elit,<br>sed do eiusmod tempor incidunt</p></div>
    <div><h4>24/7 Support</h4><p>Krytoplan consectetur adipiscing elit,<br>sed do eiusmod tempor incidunt</p></div>
  </div>
  <div class="team" style="left:170px" role="img" aria-label="Photo of two businessmen in suits seen from behind"></div>
  <div class="team" style="left:660px" role="img" aria-label="Photo of two businessmen pointing at a presentation"></div>
</section>

<section class="section plan">
  <svg width="560" height="300" viewBox="0 0 560 300">
    <g font-family="Open Sans, sans-serif" font-size="9" fill="#8a909a">
      <text x="6" y="24">80</text><text x="6" y="78">60</text><text x="6" y="132">40</text><text x="6" y="186">20</text><text x="10" y="240">0</text>
      <text x="134" y="254">2</text><text x="220" y="254">4</text><text x="306" y="254">6</text><text x="392" y="254">8</text><text x="474" y="254">10</text>
      <text x="2" y="266">Total Version</text>
    </g>
    <line x1="24" y1="237" x2="540" y2="237" stroke="#c9cdd3"/>
    <path d="M40 237 C90 237 100 80 130 80 C160 80 170 237 220 237 Z" fill="#14806b"/>
    <path d="M110 237 C170 237 180 34 218 34 C256 34 266 237 326 237 Z" fill="#153e7a"/>
    <path d="M240 237 C285 237 290 125 314 125 C338 125 343 237 388 237 Z" fill="#14806b"/>
    <path d="M320 237 C375 237 380 70 412 70 C444 70 449 237 504 237 Z" fill="#153e7a"/>
    <path d="M400 237 C445 237 450 110 478 110 C506 110 511 237 556 237 Z" fill="#14806b"/>
    <g fill="#fff"><circle cx="130" cy="80" r="2.5"/><circle cx="218" cy="34" r="2.5"/><circle cx="314" cy="125" r="2.5"/><circle cx="412" cy="70" r="2.5"/><circle cx="478" cy="110" r="2.5"/><circle cx="176" cy="212" r="2.5"/><circle cx="390" cy="212" r="2.5"/></g>
  </svg>
  <div class="kicker">We Provide Best</div>
  <h2>Financial Plan for You</h2>
  <div class="copy">
    <p>Krytoplan amet, ut perspiciatis unde omnis iste natus error sit voluptatem accusantium ipsum dolor sit amet, ctur adipiscing elit, sed do eiusmod tempor incididunt ut labore et dolore magna aliqua. Ut enim ad minim veniam, quis nostrud exercitation ullamco laboris nisi ut aliquip ex ea commodo consequatur</p>
    <p>Krytoplan amet, ut perspiciatis unde omnis iste natus error sit voluptatem accusantium que laudantium, totam rem aperiam, eaque ipsa quae ab illo inventore veritatis ipsum dolor sit amet, consectetur</p>
  </div>
  <div class="btn-outline">LEARN MORE</div>
</section>

<section class="section services">
  <h2>Our Services</h2>
  <p class="lead">Krytoplan amet sit amet, consectetur adipiscing elit, sed do eiusmod tempor incididunt ut labore et dolore magna aliqua. Ut enim ad minim veniam, quis nostrud exorcitation ullamco</p>
  <div class="service-grid">
    <div class="service"><svg width="30" height="30" viewBox="0 0 30 30"><rect x="6" y="4" width="18" height="22" fill="none" stroke="#8a909a" stroke-width="1.5"/><line x1="10" y1="11" x2="20" y2="11" stroke="#8a909a" stroke-width="1.5"/><line x1="10" y1="17" x2="20" y2="17" stroke="#8a909a" stroke-width="1.5"/></svg><h4>Financial Planning</h4><p>Krytoplan consectetur adipiscing elit, sed do eiusmod tempor incidunt</p></div>
    <div class="service"><svg width="30" height="30" viewBox="0 0 30 30"><circle cx="15" cy="15" r="10" fill="none" stroke="#8a909a" stroke-width="1.5"/><line x1="15" y1="9" x2="15" y2="21" stroke="#8a909a" stroke-width="1.5"/></svg><h4>Cash Investment</h4><p>Krytoplan consectetur adipiscing elit, sed do eiusmod tempor incidunt</p></div>
    <div class="service"><svg width="30" height="30" viewBox="0 0 30 30"><rect x="4" y="9" width="22" height="15" fill="none" stroke="#8a909a" stroke-width="1.5"/><path d="M11 9V5h8v4" fill="none" stroke="#8a909a" stroke-width="1.5"/></svg><h4>Financial Consultancy</h4><p>Krytoplan consectetur adipiscing elit, sed do eiusmod tempor incidunt</p></div>
    <div class="service"><svg width="30" height="30" viewBox="0 0 30 30"><path d="M4 18l7-6 5 4 10-9" fill="none" stroke="#8a909a" stroke-width="1.5"/><path d="M6 24h18" stroke="#8a909a" stroke-width="1.5"/></svg><h4>Personal Insurance</h4><p>Krytoplan consectetur adipiscing elit, sed do eiusmod tempor incidunt</p></div>
    <div class="service"><svg width="30" height="30" viewBox="0 0 30 30"><rect x="5" y="14" width="5" height="11" fill="none" stroke="#8a909a" stroke-width="1.5"/><rect x="13" y="9" width="5" height="16" fill="none" stroke="#8a909a" stroke-width="1.5"/><rect x="21" y="5" width="5" height="20" fill="none" stroke="#8a909a" stroke-width="1.5"/></svg><h4>Commodities Planning</h4><p>Krytoplan consectetur adipiscing elit, sed do eiusmod tempor incidunt</p></div>
    <div class="service"><svg width="30" height="30" viewBox="0 0 30 30"><circle cx="15" cy="15" r="10" fill="none" stroke="#8a909a" stroke-width="1.5"/><path d="M15 9v6l4 3" fill="none" stroke="#8a909a" stroke-width="1.5"/></svg><h4>Retirement Planning</h4><p>Krytoplan consectetur adipiscing elit, sed do eiusmod tempor incidunt</p></div>
  </div>
</section>

<section class="section banner">
  <h2>We Provide Best Financial Services for your Business</h2>
  <p>We have over 25 year's of experience in Finance and Business management so we can make your business more successful you can trust us and we care about it</p>
  <div class="btn-buy">BUY NOW</div>
</section>

<section class="section why">
  <div class="photo ph" role="img" aria-label="Photo of a businesswoman with colleagues meeting around a laptop"></div>
  <div class="kicker">Why You</div>
  <h2>Choose Krytoplan</h2>
  <p class="copy">Krytoplan amet, ut perspiciatis unde omnis iste natus error sit voluptatem accusantium ipsum dolor sit amet, ctur adipiscing elit, sed do eiusmod tempor incididunt ut labore et dolore magna aliqua.</p>
  <div class="why-grid">
    <div class="why-item"><svg width="30" height="30" viewBox="0 0 30 30"><path d="M5 25l5-5M10 20l12-14 3 3-14 12z" fill="none" stroke="#5d6470" stroke-width="1.5"/></svg><h4>Fast Loan Approval</h4><p>Krytoplan consectetur adipiscing elit, sed do eiusmod tempor incidint</p></div>
    <div class="why-item"><svg width="34" height="30" viewBox="0 0 34 30"><circle cx="11" cy="10" r="4" fill="none" stroke="#5d6470" stroke-width="1.5"/><circle cx="23" cy="10" r="4" fill="none" stroke="#5d6470" stroke-width="1.5"/><path d="M3 24c1-5 5-7 8-7s7 2 8 7M15 24c1-5 5-7 8-7s7 2 8 7" fill="none" stroke="#5d6470" stroke-width="1.5"/></svg><h4>Dedicated Team</h4><p>Krytoplan consectetur adipiscing elit, sed do eiusmod tempor incidint</p></div>
    <div class="why-item"><svg width="30" height="30" viewBox="0 0 30 30"><rect x="7" y="4" width="16" height="22" fill="none" stroke="#5d6470" stroke-width="1.5"/><path d="M11 15l3 3 6-6" fill="none" stroke="#5d6470" stroke-width="1.5"/></svg><h4>Free Documentation</h4><p>Krytoplan consectetur adipiscing elit, sed do eiusmod tempor incidint</p></div>
    <div class="why-item"><svg width="30" height="30" viewBox="0 0 30 30"><path d="M24 12a10 10 0 1 0 0 6" fill="none" stroke="#5d6470" stroke-width="1.5"/><path d="M24 6v6h-6" fill="none" stroke="#5d6470" stroke-width="1.5"/></svg><h4>Refinancing</h4><p>Krytoplan consectetur adipiscing elit, sed do eiusmod tempor incidint</p></div>
  </div>
</section>

<section class="section engage">
  <h3 style="left:52px">Reqeust a Call Back</h3>
  <p class="intro" style="left:52px">Krytoplan amet sit amet, consectetur adipiscing elit, sed do eiusmod tempor incididunt ut labore et dolore magna aliqua enim ad minim veniam</p>
  <div class="field" style="left:52px;top:272px;width:248px">Name</div>
  <div class="field" style="left:338px;top:272px;width:248px">Email</div>
  <div class="field" style="left:52px;top:322px;width:248px">Subject</div>
  <div class="field" style="left:338px;top:322px;width:248px">Phone</div>
  <div class="field" style="left:52px;top:372px;width:534px;height:132px">Message</div>
  <div class="btn-submit">SUBMIT NOW</div>

  <h3 style="left:670px">Frequently Ask Qustion</h3>
  <p class="intro" style="left:670px">Krytoplan amet sit amet, consectetur adipiscing elit, sed do eiusmod tempor incididunt ut labore et dolore magna aliqua enim ad minim veniam</p>
  <div class="faq">
    <div class="faq-item open"><span class="mark">−</span>What kind of Financial Consultancy you need</div>
    <p class="answer">Sed ut perspiciatis unde omnis iste natus error sit voluptatem accusantium doloremque laudantium totam rem, eaque ipsa quae ab illo invet</p>
    <div class="faq-item"><span class="mark">+</span>How we help you for your Business</div>
    <div class="faq-item"><span class="mark">+</span>Financial Advice</div>
    <div class="faq-item"><span class="mark">+</span>What is the best Business plan for you</div>
    <div class="faq-item"><span class="mark">+</span>Which is the right plan for Retirement</div>
  </div>
</section>

<footer class="section footer">
  <div class="brand">KRYTOPLAN.CZ</div>
  <p class="about-text">Lorem must explain to you how all this mistaolt cing pleasure and praising pain wasnad I will give you a complete pain was praspiam ta you lorem</p>
  <div class="newsletter">Email for Newsletter</div>
  <div class="col" style="left:393px">
    <h4>POPULAR POST</h4>
    <div class="post"><b>Duplex Villa Design</b>Lorem ipsum dolor sit amet, tur acinght sed do eius</div>
    <div class="post"><b>Real Estate Fest</b>Lorem ipsum dolor sit amet, tur acinght sed do eius</div>
  </div>
  <div class="col" style="left:680px">
    <h4>QUICK LINK</h4>
    <ul><li>About Us</li><li>Services</li><li>Projects</li><li>CASES</li><li>From Blog</li><li>Contact</li></ul>
  </div>
  <div class="col" style="left:916px">
    <h4>CONTACT US</h4>
    <div class="contact-row"><svg width="14" height="18" viewBox="0 0 14 18"><path d="M7 17s6-6 6-10A6 6 0 0 0 1 7c0 4 6 10 6 10z" fill="none" stroke="#c3cbdb" stroke-width="1.4"/><circle cx="7" cy="7" r="2" fill="#c3cbdb"/></svg><div>Rivermoor,<br>Lakeshire</div></div>
    <div class="contact-row"><svg width="14" height="16" viewBox="0 0 14 16"><path d="M3 1l3 3-1.5 2c.8 2 2 3.2 4 4L10 8.5l3 3-2 2.5C6 14 1 8 1 3z" fill="none" stroke="#c3cbdb" stroke-width="1.3"/></svg><div>Telephone : (+91) 555-014-2309<br>Telephone : (+91) 555-014-2309</div></div>
    <div class="contact-row"><svg width="14" height="14" viewBox="0 0 14 14"><circle cx="7" cy="7" r="6" fill="none" stroke="#c3cbdb" stroke-width="1.3"/></svg><div>Email : hello@krytoplan.cz<br>Web : www.brenvalo.com</div></div>
  </div>
</footer>
<div class="section copyright">Copyright© 2017 Krytoplan.cz. All rights reserved.</div>

</body>
</html>
```